Float and wellness centre needs a website refresh

Our float and wellness centre has been operating in Brisbane, Australia for 3 months. Our website is functional and easy to use, but it lacks a compelling visual experience that sells our awesome services to our customers.<br/><br/>We would like a complete redesign of our webpage. It is very important that the redesign considers the page layout for mobile users and the winning design will need to show both a desktop and mobile version of each of the pages listed below.<br/><br/>Out current website can be found at https://www.ommivitalityhaven.com.au/<br/><br/>The winning design will need to provide proposals for redesigning the 4 pages listed below:<br/>Home Page - https://www.ommivitalityhaven.com.au/<br/>Float Page - https://www.ommivitalityhaven.com.au/services/float<br/>Build Gift Card page - https://www.ommivitalityhaven.com.au/giftcard/stepone?location=kelverdale<br/>Booking Page - https://www.ommivitalityhaven.com.au/Calendar/Day?centerId=kelverdale&selectedCategory=FLOAT&date=12/18/2019%2000:00:00%20+10:00&sessionLength=60<br/><br/>We only need the 4 pages listed above as our web developer will use the assets from the above pages to standardize all the other pages in the site. It is very important your proposed pages contain the same information as our current pages so that we can properly see the complete layout.<br/><br/>The Home page must display the business logo in some way. We would like the website to have a white background and for it make tasteful use of color to highlight key features on the pages. Where color is used it should harmonize with the business logo. The website needs to feel bright, simple and relaxing. Our current site does not use images very well and we have had professional photos taken of the center and the float rooms specifically for this website project. You can download these, and the business logo images here: http://ommivitalityhaven.com.au/websiteimages.zip <br/><br/>We have included a few links below to other centers who have pages that we like: <br/><br/>https://www.driftquietlyhere.com/ <br/>https://www.lullnook.com.au/ <br/>https://www.skylinedrift.com.au/<br/>

Industry/Entity Type

Health And Wellness

Number of Pages Required

4 page

Font styles to use
Sans Serif

Colors

Designer to choose colors to be used in the design.

Requirements
Must have
• It is very important your proposed pages contain the same information as our current pages so that we can properly see the complete layout.
• The Home page must display the business logo in some way.
• Where color is used it should harmonize with the business logo.
Nice to have
• The website needs to feel bright, simple and relaxing. Our current site does not use images very well and we have had professional photos taken of the center and the float rooms specifically for this website project. You can download these, and the business logo images here: http://ommivitalityhaven.com.au/websiteimages.zip
Should not have
• Dark pages.

```html
<!DOCTYPE html>
<html lang="en">
<head>
<meta charset="utf-8">
<title>OMMI Gift Cards</title>
<link rel="stylesheet" href="https://fonts.googleapis.com/css2?family=Source+Sans+3:wght@400;600;700&display=swap">
<style>
:root{
  --canvas:#fcf9fa;
  --blush:#e7cddb;
  --plum:#9e5a82;
  --card-tint:#f4ecf1;
  --white:#ffffff;
  --ink:#4b4b4b;
  --ribbon-edge:#5a74c2;
  --login:#c7f0f2;
  --nav:#fdf3f7;
}
*{box-sizing:border-box;margin:0;padding:0}
html,body{width:1200px;height:1200px;overflow:hidden}
body{background:var(--canvas);font-family:"Source Sans 3",sans-serif;position:relative}
.shapes{position:absolute;left:0;top:0}
.abs{position:absolute}
.brand{left:356px;top:153px;display:flex;align-items:center;gap:2px;font-size:6px;font-weight:700;color:var(--white)}
.brand-dot{width:6px;height:6px;border-radius:50%;background:var(--plum)}
.nav{top:151px;font-size:5.5px;font-weight:600;color:var(--nav);white-space:nowrap}
.nav.current{color:var(--plum)}
.nav.login{color:var(--login)}
.hero-title{left:402px;top:184px;font-size:16.5px;line-height:22px;font-weight:600;letter-spacing:.5px;color:var(--white)}
.hero-title .brand-word{color:var(--plum)}
.card-copy{font-size:4.6px;color:var(--ink);text-align:center;line-height:6.5px}
.btn{background:var(--plum);color:var(--white);font-size:3.2px;font-weight:700;border-radius:5px;display:flex;align-items:center;justify-content:center;letter-spacing:.1px;white-space:nowrap}
.ribbon-label{font-size:8.6px;font-weight:700;color:var(--white);white-space:nowrap;transform-origin:left top}
.footer-links{left:357px;top:616px;width:78px;text-align:center;font-size:4.6px;line-height:6.5px;color:var(--white)}
.footer-mid{left:505px;top:630px;width:50px;text-align:center;font-size:4.6px;line-height:6.5px;color:var(--white)}
.footer-brand{left:480px;top:598px;width:100px;text-align:center;font-size:7px;font-weight:600;color:var(--white);letter-spacing:.4px}
.footer-brand .brand-dot{display:block;margin:0 auto 3px;width:14px;height:14px;background:var(--white)}
.follow{left:648px;top:620px;width:40px;text-align:center;font-size:4.6px;font-weight:700;color:var(--white)}
.social{top:628px;width:9px;height:9px;border:1px solid var(--white);border-radius:2px}
</style>
</head>
<body>
<svg class="shapes" width="1200" height="1200" viewBox="0 0 1200 1200">
  <defs>
    <linearGradient id="hero-glow" x1="0" y1="0" x2="0" y2="1">
      <stop offset="0" stop-color="#efa3a9"/>
      <stop offset=".45" stop-color="#ea8fbe"/>
      <stop offset=".75" stop-color="#b7a6d2"/>
      <stop offset="1" stop-color="#86c3c8"/>
    </linearGradient>
    <linearGradient id="gift-icon" x1="0" y1="0" x2="0" y2="1">
      <stop offset="0" stop-color="#c0268f"/>
      <stop offset=".6" stop-color="#7d49a6"/>
      <stop offset="1" stop-color="#3fbfae"/>
    </linearGradient>
    <linearGradient id="redeem-icon" x1="0" y1="0" x2="0" y2="1">
      <stop offset="0" stop-color="#f2c531"/>
      <stop offset=".45" stop-color="#8e3aa2"/>
      <stop offset="1" stop-color="#3fbfae"/>
    </linearGradient>
    <clipPath id="hero-clip"><polygon points="350,143 696,143 696,265 523,304 350,265"/></clipPath>
  </defs>

  <polygon class="hero-band" points="350,143 696,143 696,265 523,304 350,265" fill="var(--blush)"/>
  <circle clip-path="url(#hero-clip)" cx="562" cy="224" r="68" fill="url(#hero-glow)" opacity=".55" role="img" aria-label="Soft gradient backdrop for the gift card hero"/>

  <rect x="398" y="314" width="108" height="182" rx="4" fill="var(--card-tint)"/>
  <rect x="408" y="367" width="86" height="120" rx="3" fill="var(--white)"/>
  <polygon points="392,318 398,317 398,321" fill="var(--ribbon-edge)"/>
  <polygon points="512,355 506,358 506,354" fill="var(--ribbon-edge)"/>
  <polygon points="392,320 512,343 512,357 392,333" fill="var(--plum)"/>
  <polygon points="451,379 471,390 471,412 451,423 431,412 431,390" fill="url(#gift-icon)" role="img" aria-label="Gift card icon"/>

  <rect x="547" y="345" width="108" height="182" rx="4" fill="var(--card-tint)"/>
  <rect x="558" y="398" width="86" height="120" rx="3" fill="var(--white)"/>
  <polygon points="541,349 547,348 547,352" fill="var(--ribbon-edge)"/>
  <polygon points="661,387 655,390 655,386" fill="var(--ribbon-edge)"/>
  <polygon points="541,351 661,375 661,389 541,364" fill="var(--plum)"/>
  <rect x="581" y="412" width="40" height="44" rx="6" fill="url(#redeem-icon)" opacity=".85" role="img" aria-label="Hand receiving a gift card coin"/>

  <polygon class="footer-band" points="357,600 530,568 703,600 703,650 357,650" fill="var(--plum)"/>
</svg>

<div class="abs brand"><span class="brand-dot"></span>OMMI</div>
<span class="abs nav" style="left:457px">Home</span>
<span class="abs nav" style="left:487px">Float</span>
<span class="abs nav" style="left:514px">IR Sauna</span>
<span class="abs nav" style="left:551px">mHBOT</span>
<span class="abs nav" style="left:584px">Heat Mat</span>
<span class="abs nav current" style="left:618px">Gift cards</span>
<span class="abs nav login" style="left:656px">Login</span>

<h1 class="abs hero-title"><span class="brand-word">OMMI</span><br>GIFT<br>CARDS.</h1>

<div class="abs ribbon-label" style="left:428px;top:324px;transform:rotate(11deg)">Build gift card</div>
<p class="abs card-copy" style="left:408px;top:441px;width:86px">Click below to build a gift card</p>
<div class="abs btn" style="left:432px;top:468px;width:39px;height:10px">BUILD GIFT CARD</div>

<div class="abs ribbon-label" style="left:569px;top:356px;transform:rotate(11deg)">Reedem gift card</div>
<p class="abs card-copy" style="left:570px;top:472px;width:68px">If you already have a gift card<br>click below</p>
<div class="abs btn" style="left:582px;top:499px;width:39px;height:10px">REEDEM GIFT CARD</div>

<div class="abs footer-brand"><span class="brand-dot"></span>OMMI</div>
<div class="abs footer-links">Booking Policy<br>Membership Policy<br>Privacy Policy<br>Cancellation Policy</div>
<div class="abs footer-mid">FAQs<br>Sitemap</div>
<div class="abs follow">Follow US</div>
<span class="abs social" style="left:656px" role="img" aria-label="Social link"></span>
<span class="abs social" style="left:670px" role="img" aria-label="Social link"></span>
</body>
</html>
```